Business Card Design.... Vantor logistics LLC --- Logo Included

Vantor logistics LLC is a small team trucking company....
Cards must match the website [login to view URL]
Red - Black - White

"Vantor Logistics"
"When Your Critical Freight Needs The Steady Hand Of A Seasoned Crew."

"Looking For A Reliable Team? Call To Hire Us!"

CONTEST WILL NOT LAST 5 DAYS!!!!!

```html
<!DOCTYPE html>
<html lang="en">
<head>
<meta charset="utf-8">
<title>Vantor Logistics LLC — Business Card</title>
<link rel="stylesheet" href="https://fonts.googleapis.com/css2?family=Lato:wght@400;700;900&display=swap">
<style>
  :root {
    --red: #e3101a;
    --red-deep: #b00b12;
    --black: #0b0b0b;
    --bevel: #1b1b1b;
    --bevel-line: #2e2e2e;
    --white: #ffffff;
    --muted: #d6d6d6;
    --backdrop: #d9dadd;
  }
  * { margin: 0; padding: 0; box-sizing: border-box; }
  html, body {
    width: 1200px; height: 900px; overflow: hidden;
    background: var(--backdrop);
    font-family: "Lato", Arial, sans-serif;
  }
  .canvas {
    position: relative; width: 1200px; height: 900px;
    display: flex; flex-direction: column; align-items: center; justify-content: center; gap: 40px;
  }
  .card {
    position: relative; width: 680px; height: 388px; overflow: hidden;
    background: var(--black);
    box-shadow: 0 6px 18px rgba(0,0,0,0.25);
  }
  .card-shapes { position: absolute; inset: 0; width: 100%; height: 100%; }

  .wordmark {
    position: absolute; display: flex; align-items: center; gap: 12px;
    color: var(--white); font-weight: 900; font-size: 26px; letter-spacing: 0.5px; white-space: nowrap;
  }
  .wordmark-mark { width: 16px; height: 16px; background: var(--white); flex: none; }

  /* front */
  .front .wordmark { left: 34px; top: 176px; font-size: 24px; }
  .holder { position: absolute; left: 428px; top: 70px; }
  .holder-name { color: var(--red); font-weight: 900; font-size: 30px; letter-spacing: 1px; }
  .holder-company { color: var(--white); font-size: 14px; margin-top: 4px; letter-spacing: 0.5px; }

  .contacts { position: absolute; left: 428px; top: 168px; list-style: none; display: flex; flex-direction: column; gap: 14px; }
  .contact { display: flex; align-items: flex-start; gap: 12px; color: var(--white); font-size: 13px; line-height: 1.35; }
  .contact-icon { width: 26px; height: 26px; flex: none; background: var(--red); display: flex; align-items: center; justify-content: center; }
  .contact-icon svg { width: 15px; height: 15px; }

  /* back */
  .back .wordmark { left: 44px; top: 150px; }
  .tagline {
    position: absolute; left: 432px; top: 118px; width: 228px;
    color: var(--white); font-size: 17px; font-weight: 700; line-height: 1.35; text-align: center;
  }
</style>
</head>
<body>
<main class="canvas">

  <!-- Front of card -->
  <section class="card front" aria-label="Business card front">
    <svg class="card-shapes" viewBox="0 0 680 388" aria-hidden="true">
      <polygon points="0,0 300,0 380,194 300,388 0,388" fill="var(--red)"/>
      <polygon points="300,0 336,0 416,194 336,388 300,388 380,194" fill="var(--bevel)"/>
      <polyline points="336,0 416,194 336,388" fill="none" stroke="var(--bevel-line)" stroke-width="2"/>
      <polygon points="540,388 680,388 680,250" fill="var(--red)"/>
      <polyline points="520,388 680,230" fill="none" stroke="var(--bevel)" stroke-width="14"/>
    </svg>

    <div class="wordmark"><span class="wordmark-mark"></span>Vantor Logistics LLC</div>

    <div class="holder">
      <p class="holder-name">DALEN MARSH</p>
      <p class="holder-company">Vantor Logistics LLC</p>
    </div>

    <ul class="contacts">
      <li class="contact">
        <span class="contact-icon">
          <svg viewBox="0 0 24 24"><path fill="var(--white)" d="M6.6 10.8a15.1 15.1 0 0 0 6.6 6.6l2.2-2.2a1 1 0 0 1 1-.25 11.4 11.4 0 0 0 3.6.57 1 1 0 0 1 1 1V20a1 1 0 0 1-1 1A17 17 0 0 1 3 4a1 1 0 0 1 1-1h3.5a1 1 0 0 1 1 1c0 1.25.2 2.45.57 3.57a1 1 0 0 1-.25 1z"/></svg>
        </span>
        <span>+1 6155550142<br>+1 6155550187</span>
      </li>
      <li class="contact">
        <span class="contact-icon">
          <svg viewBox="0 0 24 24"><path fill="var(--white)" d="M12 2a7 7 0 0 0-7 7c0 5.2 7 13 7 13s7-7.8 7-13a7 7 0 0 0-7-7zm0 9.5A2.5 2.5 0 1 1 12 6.5a2.5 2.5 0 0 1 0 5z"/></svg>
        </span>
        <span>214 Millstone Ridge Rd.<br>Linden Falls, TN 38099</span>
      </li>
      <li class="contact">
        <span class="contact-icon">
          <svg viewBox="0 0 24 24"><circle cx="12" cy="12" r="9" fill="none" stroke="var(--white)" stroke-width="2"/><path d="M3 12h18M12 3c3 3.2 3 14.8 0 18M12 3c-3 3.2-3 14.8 0 18" fill="none" stroke="var(--white)" stroke-width="1.6"/></svg>
        </span>
        <span>dispatch@vantorlogistics.com<br>www.vantorlogistics.com</span>
      </li>
    </ul>
  </section>

  <!-- Back of card -->
  <section class="card back" aria-label="Business card back">
    <svg class="card-shapes" viewBox="0 0 680 388" aria-hidden="true">
      <polygon points="0,0 150,0 0,130" fill="var(--red)"/>
      <polyline points="170,0 0,148" fill="none" stroke="var(--bevel)" stroke-width="14"/>
      <polygon points="420,0 680,0 680,388 340,388 400,194" fill="var(--bevel)"/>
      <polygon points="456,0 680,0 680,388 376,388 436,194" fill="var(--red)"/>
      <polyline points="420,0 400,194 340,388" fill="none" stroke="var(--bevel-line)" stroke-width="2"/>
    </svg>

    <div class="wordmark"><span class="wordmark-mark"></span>Vantor Logistics LLC</div>

    <p class="tagline">“When Your Critical Freight Needs The Steady Hand Of A Seasoned Crew. Looking For A Reliable Team? Call To Hire Us!”</p>
  </section>

</main>
</body>
</html>
```